Legal Campaign

A courier compavny that offer Legal services like filing/recording Court documents.
Updates

These info must be on card: Can We Help With Your Legal Services? Need Your Court documents quickly filed? .Filing/Recording in Erie, Niagara & Monroe County .Pick-up within 15-30 minutes of call .Medical records pick-up & delivery .Court-Authorized Process Servers .$9.00 Buffalo to Buffalo .Volume Discounts Call Drew Halvorn@716-555-0143 The address must be 48 Tillman Ave., Buffalo NY 14209

Please add the following info: 1.Post Office Pickup/Deliveries 2. Drewhalvorn@qrtlane.com

Target Market(s)

Law firms & legal community.

Industry/Entity Type

Court

Requirements
Must have
• RoutaSwift logo must be on card. Please visit the website@qrtlane.com to check out the logo. Thanks

```html
<!DOCTYPE html>
<html lang="en">
<head>
<meta charset="utf-8">
<title>Legal Services Courier Ad</title>
<link rel="stylesheet" href="https://fonts.googleapis.com/css2?family=Fira+Sans:wght@600&family=Arimo:wght@400;700&family=Roboto+Condensed:wght@700&family=Archivo+Black&family=Open+Sans:wght@700&display=swap">
<style>
  :root {
    --frame: #1f6f93;
    --header-bg: #f2f1e4;
    --headline: #ee1c24;
    --panel: #62eef3;
    --call-band: #c6f7fa;
    --ink: #111111;
    --accent: #e8141c;
    --brand-bg: #ffffff;
    --photo-light: #dfe2e6;
    --photo-mid: #b9c0ca;
    --photo-warm: #d9c65a;
    --photo-deep: #3f68b0;
  }
  * { box-sizing: border-box; margin: 0; padding: 0; }
  html, body { width: 1200px; height: 930px; overflow: hidden; background: #ffffff; }
  .ad { position: relative; width: 1200px; height: 930px; background: var(--frame); }

  .headline-band {
    position: absolute; left: 18px; top: 18px; width: 1164px; height: 152px;
    background: var(--header-bg);
    display: flex; flex-direction: column; align-items: center; justify-content: center;
  }
  .headline {
    font-family: "Fira Sans", sans-serif; font-weight: 600;
    color: var(--headline); font-size: 55px; line-height: 60px;
    text-shadow: 2px 3px 2px rgba(0,0,0,0.35);
    letter-spacing: 0.4px; white-space: nowrap;
  }

  .photo {
    position: absolute; left: 18px; top: 170px; width: 552px; height: 742px;
    background: linear-gradient(170deg, var(--photo-light) 0%, var(--photo-mid) 35%, #c9c3a0 55%, var(--photo-warm) 68%, #6f8fc4 82%, var(--photo-deep) 100%);
  }
  .brand {
    position: absolute; left: 44px; top: 824px; height: 64px; padding: 0 22px 0 16px;
    background: var(--brand-bg);
    display: flex; align-items: center; gap: 12px;
    font-family: "Arimo", sans-serif; font-weight: 700; font-size: 36px; color: var(--frame);
  }
  .brand-mark { width: 30px; height: 30px; background: var(--frame); flex: none; }

  .info-panel {
    position: absolute; left: 570px; top: 170px; width: 612px; height: 742px;
    background: var(--panel);
  }
  .services { position: absolute; left: 22px; top: 16px; list-style: none; }
  .services li {
    font-family: "Arimo", sans-serif; font-size: 34px; line-height: 44px;
    color: var(--ink); display: flex; align-items: flex-start; white-space: nowrap;
  }
  .services svg { width: 30px; height: 30px; margin-top: 5px; margin-right: 4px; flex: none; }
  .services .indent { display: block; padding-left: 12px; }

  .credential-box {
    position: absolute; left: 115px; top: 250px; width: 384px; height: 120px;
    border: 4px solid var(--ink);
    display: flex; align-items: center; justify-content: center; text-align: center;
    font-family: "Roboto Condensed", sans-serif; font-weight: 700;
    font-size: 46px; line-height: 48px; color: var(--accent);
  }

  .offers { position: absolute; left: 50px; top: 386px; list-style: none; }
  .offers li {
    font-family: "Archivo Black", sans-serif; font-size: 33px; line-height: 44px;
    color: var(--ink); display: flex; align-items: center; letter-spacing: 0.5px; white-space: nowrap;
  }
  .offers li:nth-child(2) { padding-left: 8px; }
  .offers svg { width: 28px; height: 30px; margin-right: 2px; flex: none; }

  .call-band {
    position: absolute; left: 10px; top: 490px; width: 602px; height: 150px;
    background: var(--call-band); text-align: center;
  }
  .call-name {
    font-family: "Arimo", sans-serif; font-weight: 700; font-size: 49px;
    color: var(--ink); margin-top: 10px; line-height: 58px; white-space: nowrap;
  }
  .call-phone {
    font-family: "Arimo", sans-serif; font-weight: 700; font-size: 68px;
    color: var(--accent); line-height: 78px; letter-spacing: 1px; white-space: nowrap;
  }

  .address {
    position: absolute; left: 0; top: 648px; width: 612px; text-align: center;
    font-family: "Open Sans", sans-serif; font-weight: 700;
    font-size: 23px; line-height: 29px; color: var(--ink); font-style: normal;
  }
</style>
</head>
<body>
<div class="ad">
  <header class="headline-band">
    <h1 class="headline">Can We Help With Your Legal Services?</h1>
    <h2 class="headline">Need Your Court documents quickly filed?</h2>
  </header>

  <div class="photo" role="img" aria-label="Photo of a tall stack of colourful file folders in a records archive, with a red RECEIVED stamp graphic"></div>

  <div class="brand"><span class="brand-mark"></span>RoutaSwift</div>

  <section class="info-panel">
    <ul class="services">
      <li><svg viewBox="0 0 24 24"><polygon fill="#e8141c" points="12,2 14.9,9 22.5,9.3 16.6,14 18.7,21.5 12,17.3 5.3,21.5 7.4,14 1.5,9.3 9.1,9"/></svg><span>Filing/Recording in Erie, Niagara<span class="indent">&amp; Monroe County</span></span></li>
      <li><svg viewBox="0 0 24 24"><polygon fill="#e8141c" points="12,2 14.9,9 22.5,9.3 16.6,14 18.7,21.5 12,17.3 5.3,21.5 7.4,14 1.5,9.3 9.1,9"/></svg><span>Pick-up within 15-30 minutes of call</span></li>
      <li><svg viewBox="0 0 24 24"><polygon fill="#e8141c" points="12,2 14.9,9 22.5,9.3 16.6,14 18.7,21.5 12,17.3 5.3,21.5 7.4,14 1.5,9.3 9.1,9"/></svg><span>Medical records pick-up &amp; delivery</span></li>
      <li><svg viewBox="0 0 24 24"><polygon fill="#e8141c" points="12,2 14.9,9 22.5,9.3 16.6,14 18.7,21.5 12,17.3 5.3,21.5 7.4,14 1.5,9.3 9.1,9"/></svg><span>Post Office Pickup/Deliveries</span></li>
    </ul>

    <div class="credential-box">Court-Authorized<br>Process Servers</div>

    <ul class="offers">
      <li><svg viewBox="0 0 24 26"><path d="M2 15 L6 12 L9 18 L20 2 L23 4 L9 24 Z" fill="#e8141c"/></svg>$9.00 Buffalo to Buffalo</li>
      <li><svg viewBox="0 0 24 26"><path d="M2 15 L6 12 L9 18 L20 2 L23 4 L9 24 Z" fill="#e8141c"/></svg>Volume Discounts</li>
    </ul>

    <div class="call-band">
      <p class="call-name">Call Drew Halvorn @</p>
      <p class="call-phone">716-555-0143</p>
    </div>

    <address class="address">48 Tillman Ave.<br>Buffalo NY 14209<br>Drewhalvorn@qrtlane.com</address>
  </section>
</div>
</body>
</html>
```